Business Card and Letterhead for Nurlo - modern real estate business

I need a double sided business card design for Nurlo. Please see business card brief here https://papers.trelvimo.net/sheet/q/7XrTbaLeZpMmQ2uWvd9HkCj4yNoEfsGi3lRtAz_pk/view?mode=shared

Please feel free to design the business cards however you feel best. I am happy to give some creative freedoms and then provide feedback from there.

Please then also create a letterhead to match the business card design

Colors

Designer to choose colors to be used in the design.

Requirements
Must have
• Must be a modern, elegant business card which looks very professional

```html
<!DOCTYPE html>
<html lang="en">
<head>
<meta charset="utf-8">
<title>Nurlo Business Card</title>
<link href="https://fonts.googleapis.com/css2?family=Roboto:wght@400;500;700;900&display=swap" rel="stylesheet">
<style>
  :root {
    --page-bg: #3a3a3c;
    --card-dark: #1a1a1c;
    --card-mid: #262628;
    --band: #0e0e0f;
    --accent-red: #e31b23;
    --text-white: #f2f2f2;
    --logo-silver: #c4c4c6;
    --photo-light: #5e5e60;
    --photo-mid: #333335;
    --photo-suit: #2a2c30;
    --photo-dark: #151516;
  }
  * { margin: 0; padding: 0; box-sizing: border-box; }
  html, body { width: 1200px; height: 960px; overflow: hidden; }
  body {
    background: var(--page-bg);
    font-family: "Roboto", Arial, sans-serif;
    position: relative;
  }
  .card {
    position: absolute;
    left: 240px;
    width: 720px;
    height: 410px;
    border-radius: 22px;
    overflow: hidden;
    background: linear-gradient(135deg, var(--card-mid), var(--card-dark));
    box-shadow: 0 14px 30px rgba(0,0,0,0.45);
  }
  .card-back { top: 40px; }
  .card-front { top: 510px; }

  .back-wordmark {
    position: absolute;
    inset: 0;
    display: flex;
    align-items: center;
    justify-content: center;
    font-weight: 700;
    font-size: 120px;
    letter-spacing: 6px;
    color: var(--logo-silver);
  }

  .front-art { position: absolute; inset: 0; }

  .front-wordmark {
    position: absolute;
    left: 40px;
    top: 34px;
    font-weight: 700;
    font-size: 52px;
    line-height: 60px;
    letter-spacing: 2px;
    color: var(--accent-red);
  }
  .company-details {
    position: absolute;
    left: 44px;
    top: 100px;
    list-style: none;
    color: var(--accent-red);
    font-size: 15px;
    line-height: 22px;
  }
  .company-details li { display: flex; align-items: center; gap: 8px; }
  .icon { width: 13px; height: 13px; flex: none; }

  .agent-name {
    position: absolute;
    left: 40px;
    top: 234px;
    color: var(--accent-red);
    font-weight: 700;
    font-size: 28px;
    line-height: 30px;
  }
  .agent-title {
    position: absolute;
    left: 40px;
    top: 266px;
    color: var(--text-white);
    font-size: 16px;
    line-height: 18px;
  }
  .agent-details {
    position: absolute;
    left: 40px;
    top: 300px;
    list-style: none;
    color: var(--text-white);
    font-size: 17px;
    line-height: 23px;
  }
  .agent-details li { display: flex; align-items: center; gap: 8px; }
  .label-red { color: var(--accent-red); }
</style>
</head>
<body>

  <section class="card card-back">
    <div class="back-wordmark">NURLO</div>
  </section>

  <section class="card card-front">
    <svg class="front-art" width="720" height="410" viewBox="0 0 720 410">
      <defs>
        <radialGradient id="portraitTone" cx="0.5" cy="0.25" r="0.75">
          <stop offset="0" stop-color="var(--photo-light)"/>
          <stop offset="0.55" stop-color="var(--photo-mid)"/>
          <stop offset="1" stop-color="var(--photo-dark)"/>
        </radialGradient>
        <linearGradient id="portraitShade" x1="0" y1="0" x2="0" y2="1">
          <stop offset="0.45" stop-color="var(--photo-suit)" stop-opacity="0"/>
          <stop offset="1" stop-color="var(--photo-suit)" stop-opacity="0.9"/>
        </linearGradient>
      </defs>
      <rect class="name-band" x="0" y="226" width="430" height="64" fill="var(--band)"/>
      <g role="img" aria-label="Portrait photo of the agent in a dark suit against a grey backdrop">
        <circle class="portrait-area" cx="640" cy="40" r="320" fill="url(#portraitTone)"/>
        <circle class="portrait-shade" cx="640" cy="40" r="320" fill="url(#portraitShade)"/>
      </g>
      <circle class="portrait-ring" cx="640" cy="40" r="320" fill="none"
              stroke="var(--accent-red)" stroke-width="4"/>
    </svg>

    <div class="front-wordmark">NURLO</div>

    <ul class="company-details">
      <li>Lic No. 10472318</li>
      <li>
        <svg class="icon" viewBox="0 0 16 16"><path d="M3 1h3l1.5 4-2 1.5a9 9 0 0 0 4 4L11 8.5l4 1.5v3c0 1-1 2-2 2A13 13 0 0 1 1 3c0-1 1-2 2-2z" fill="currentColor"/></svg>
        02 4810 3927
      </li>
      <li>
        <svg class="icon" viewBox="0 0 16 16"><rect x="1" y="3" width="14" height="10" rx="1" fill="currentColor"/><path d="M1.5 4 8 9l6.5-5" stroke="#1c1c1e" stroke-width="1.4" fill="none"/></svg>
        info@nurlo.com
      </li>
      <li>
        <svg class="icon" viewBox="0 0 16 16"><circle cx="8" cy="8" r="7" fill="currentColor"/><path d="M1 8h14M8 1c3 3 3 11 0 14M8 1c-3 3-3 11 0 14" stroke="#1c1c1e" stroke-width="1" fill="none"/></svg>
        www.nurlo.com
      </li>
    </ul>

    <h1 class="agent-name">Liam Corder</h1>
    <p class="agent-title">Licenced Real Estate Agent</p>

    <ul class="agent-details">
      <li><span class="label-red">Lic No.</span> 20381946</li>
      <li>
        <svg class="icon label-red" viewBox="0 0 16 16"><path d="M3 1h3l1.5 4-2 1.5a9 9 0 0 0 4 4L11 8.5l4 1.5v3c0 1-1 2-2 2A13 13 0 0 1 1 3c0-1 1-2 2-2z" fill="currentColor"/></svg>
        0451 630 218
      </li>
      <li>
        <svg class="icon label-red" viewBox="0 0 16 16"><rect x="1" y="3" width="14" height="10" rx="1" fill="currentColor"/><path d="M1.5 4 8 9l6.5-5" stroke="#1c1c1e" stroke-width="1.4" fill="none"/></svg>
        liam@nurlo.com
      </li>
      <li>PO Box 3194 Carrowvale NSW 2790</li>
    </ul>
  </section>

</body>
</html>
```